依頼概要
■依頼の目的/概要
当方、鍼灸サロン店を運営しております。
メニューのデザインも新しいものに一新しようと考えております。

■要望ポイント
高級感のあれイメージでありつつもカフェや美容クリニックのような美的でおしゃれなデザインを希望致します。女性の方が多く利用されています。
古風なものは好ましくないです。

また新たに出張施術のサービスも、開始するためそのメニュー表の作成もお願いします。

■その他注意点など
店内の写真等HP、予約サイトもお送り致しますので、ある程度統一感のあるデザインにして頂きたいです。

その他何かご不明な点がございましたら、お気軽にご質問下さい。
よろしくお願いいたします。
メニュー表で出張施術を90分20000円〜交通費要相談
を新たに1ページ追加してほしいです。
■ 選んだ理由

デザインが良かったです。

■ 提案者全員のお礼・コメント

ありがとうございました。

```html
<!DOCTYPE html>
<html lang="ja">
<head>
<meta charset="utf-8">
<title>施術メニュー</title>
<link href="https://fonts.googleapis.com/css2?family=Great+Vibes&family=Shippori+Mincho:wght@400;500;600&family=Cormorant+Garamond:ital,wght@1,500&display=swap" rel="stylesheet">
<style>
:root{
  --mint:#dcefec;
  --paper:#ffffff;
  --gold:#b59a5e;
  --gold-soft:#d9c89d;
  --gold-pale:#f3ecd9;
  --gold-wash:#faf7ee;
  --ink:#3a3a3a;
  --ink-soft:#6a6a6a;
}
*{margin:0;padding:0;box-sizing:border-box}
html,body{width:846px;height:1200px;overflow:hidden}
body{background:var(--mint);font-family:"Shippori Mincho",serif;color:var(--ink);position:relative}
.sheet{position:absolute;left:52px;top:40px;width:744px;height:1122px;background:var(--paper);border:2px solid var(--gold-soft);outline:1px solid var(--gold-soft);outline-offset:-9px}
.abs{position:absolute}
.title{left:0;right:0;top:78px;text-align:center}
.title h1{font-family:"Great Vibes",cursive;font-weight:400;font-size:96px;color:var(--gold);line-height:1}
.title p{font-size:14px;letter-spacing:.25em;color:var(--gold);margin-top:4px}
.title-rule{left:300px;width:246px;top:232px;height:1px;background:var(--gold-soft)}
.heading{left:82px;right:82px;text-align:center}
.heading h2{font-weight:500;font-size:40px;letter-spacing:.12em;line-height:1.1}
.heading .rule{height:5px;border-top:1px solid var(--gold);border-bottom:1px solid var(--gold);margin-top:6px}
.desc{left:90px;right:90px;font-size:11.5px;line-height:17px;color:var(--ink-soft)}
.price-table{left:100px;border-collapse:collapse}
.price-table th{font-weight:400;font-size:11px;height:24px;width:140px;border:1px solid var(--gold-soft);color:var(--ink-soft)}
.price-table th.repeat{background:var(--gold-pale);color:var(--ink)}
.price-table th.blank{border:none;width:160px}
.price-table td{height:29px;border-bottom:1px dotted var(--gold-soft);text-align:center;font-size:15px}
.price-table td.name{text-align:left;font-size:13.5px;padding-left:4px;line-height:1.4}
.price-table td.repeat{background:var(--gold-wash);font-weight:600}
.yen{font-size:10px;margin-left:1px}
.option{left:590px;width:186px;border:1px solid var(--gold-soft);padding:7px 12px 9px;text-align:center}
.option .label{font-family:"Cormorant Garamond",serif;font-style:italic;font-size:21px;color:var(--gold);line-height:1}
.option .sub{font-size:8.5px;color:var(--gold);letter-spacing:.2em}
.option .row{font-size:13.5px;margin-top:5px;display:flex;justify-content:space-between}
.note{left:104px;font-size:9.5px;color:var(--ink-soft)}
.footer-note{left:0;right:0;top:1112px;text-align:center;font-size:10px;color:var(--ink-soft)}
</style>
</head>
<body>
<div class="sheet"></div>

<header class="abs title">
  <h1>Menu</h1>
  <p>施術メニュー</p>
</header>
<div class="abs title-rule"></div>

<div class="abs heading" style="top:330px"><h2>鍼灸</h2><div class="rule"></div></div>
<p class="abs desc" style="top:400px">お体の状態に合わせて、お悩みを根本からととのえていきます。<br>鍼灸と整体を組み合わせ、お一人おひとりに合わせたオーダーメイドの施術です。<br>肩こり・腰痛・冷えなど、日々の不調を優しくケアいたします。</p>
<table class="abs price-table" style="top:458px">
  <tr><th class="blank"></th><th>初回の方</th><th class="repeat">2回目以降の方</th></tr>
  <tr><td class="name">鍼灸&amp;整体 60分</td><td>7,600<span class="yen">円</span></td><td class="repeat">6,600<span class="yen">円</span></td></tr>
  <tr><td class="name">鍼灸&amp;整体 90分</td><td>9,800<span class="yen">円</span></td><td class="repeat">8,800<span class="yen">円</span></td></tr>
  <tr><td class="name">鍼灸&amp;整体 120分</td><td>12,000<span class="yen">円</span></td><td class="repeat">11,000<span class="yen">円</span></td></tr>
</table>
<aside class="abs option" style="top:500px">
  <div class="label">Option menu</div><div class="sub">オプションメニュー</div>
  <div class="row"><span>延長15分</span><span>2,200<span class="yen">円</span></span></div>
</aside>
<p class="abs note" style="top:578px">※初回のお客様は、施術料とは別に1,000円(税込)頂戴します。</p>

<div class="abs heading" style="top:620px"><h2>美容鍼</h2><div class="rule"></div></div>
<p class="abs desc" style="top:690px">お顔に細い鍼を打つことによって、美しいフェイスラインへ導きます。<br>新陳代謝を高めてハリのある、うるおい肌を目指します。</p>
<table class="abs price-table" style="top:734px">
  <tr><th class="blank"></th><th>初回の方</th><th class="repeat">2回目以降の方</th></tr>
  <tr><td class="name">美容鍼 30分</td><td>5,400<span class="yen">円</span></td><td class="repeat">4,400<span class="yen">円</span></td></tr>
</table>
<p class="abs note" style="top:796px">※初回のお客様は、施術料とは別に1,000円(税込)頂戴します。</p>

<div class="abs heading" style="top:826px"><h2>水素灸</h2><div class="rule"></div></div>
<p class="abs desc" style="top:896px">水素の熱気で、不調の箇所をピンポイントで温めます。<br>水素の働きで、老廃物の排出を促し体質改善をサポートします。<br>※体質改善を目的とした施術です。オプションもお選びいただけます。</p>
<table class="abs price-table" style="top:970px">
  <tr><th class="blank"></th><th>初回の方</th><th class="repeat">2回目以降の方</th></tr>
  <tr><td class="name">体質改善<br>全身水素灸 30分</td><td>6,500<span class="yen">円</span></td><td class="repeat">5,500<span class="yen">円</span></td></tr>
</table>
<aside class="abs option" style="top:976px">
  <div class="label">Option menu</div><div class="sub">オプションメニュー</div>
  <div class="row"><span>延長15分</span><span>2,200<span class="yen">円</span></span></div>
</aside>
<p class="abs note" style="top:1060px">※初回のお客様は、施術料とは別に1,000円(税込)頂戴します。</p>

<p class="abs footer-note">※表示価格はすべて税込価格です。</p>
</body>
</html>
```